ALL TYPES OF COMMERCIAL PLASTERING

TYPE OF BLOCK LETTERING WITH STAND OUT QUALITIES
WITH SOME TYPE OF LOGO
SOMETHING UNIQUE FOR THE BUILDING INDUSTRY.
QUALITY WORKMANSHIP
Updates

forgot to include my mobile phone number on my brief. could you add it to your design please MOBILE PH 0418 695 031

please let me make this quite clear ,the company name is northgate linings and Fitouts PTY LTD. THE TYPE OF WORK WE WILL BE DOING IS COMMERCIAL PLASTERING.

Industry/Entity Type

Industry

Contact Information for Business Card

northgate linings and fitouts P/L
martin corbell p.o.box 42 wendouree 3355 email address northgatelinings@mailbox-example.com
ABN 51 847 213 906 COMMERCIAL PLASTERING

```html
<!DOCTYPE html>
<html lang="en">
<head>
<meta charset="utf-8">
<title>Northgate Linings and Fitouts – Business Card</title>
<link rel="stylesheet" href="https://fonts.googleapis.com/css2?family=Bebas+Neue&family=Poiret+One&display=swap">
<style>
  :root {
    --paper: #ffffff;
    --band: #eba9aa;
    --ink: #2b1410;
  }
  html, body {
    margin: 0;
    padding: 0;
    overflow: hidden;
    background: var(--paper);
  }
  .card {
    position: relative;
    width: 1200px;
    height: 664px;
    background: var(--paper);
    color: var(--ink);
    overflow: hidden;
  }
  .band {
    position: absolute;
    left: 0;
    top: 187px;
    width: 1200px;
    height: 137px;
    background: var(--band);
  }
  .headline {
    position: absolute;
    left: 269px;
    top: 206px;
    margin: 0;
    font-family: "Bebas Neue", "Oswald", sans-serif;
    font-weight: 400;
    font-size: 58px;
    line-height: 1;
    letter-spacing: 3.9px;
    color: var(--ink);
    -webkit-text-stroke: 0.8px var(--ink);
  }
  .services {
    position: absolute;
    left: 352px;
    top: 271px;
    margin: 0;
    font-family: "Bebas Neue", "Oswald", sans-serif;
    font-weight: 400;
    font-size: 34px;
    line-height: 1;
    letter-spacing: 6.4px;
    color: var(--ink);
    -webkit-text-stroke: 0.5px var(--ink);
  }
  .company-name {
    position: absolute;
    left: 818px;
    top: 210px;
    width: 150px;
    margin: 0;
    font-family: "Bebas Neue", "Oswald", sans-serif;
    font-weight: 400;
    font-size: 30px;
    line-height: 0.98;
    letter-spacing: 1px;
    color: var(--ink);
  }
  .contact {
    position: absolute;
    font-family: "Poiret One", "Quicksand", sans-serif;
    font-size: 29px;
    line-height: 38px;
    letter-spacing: 3.2px;
    color: var(--ink);
    -webkit-text-stroke: 0.3px var(--ink);
  }
  .contact p { margin: 0; }
  .contact-person {
    left: 54px;
    top: 545px;
    text-transform: uppercase;
  }
  .contact-person .email {
    text-transform: none;
    letter-spacing: 0.6px;
  }
  .contact-business {
    right: 51px;
    top: 545px;
    text-align: right;
    text-transform: uppercase;
  }
</style>
</head>
<body>
  <main class="card">
    <div class="band"></div>
    <h1 class="headline">Commercial Plastering</h1>
    <h2 class="services">Linings and Fitouts</h2>
    <p class="company-name">Northgate<br>Linings and<br>Fitouts P/L</p>

    <section class="contact contact-person">
      <p>P/L Martin Corbell</p>
      <p>P.O.Box 42 Wendouree 3355</p>
      <p class="email">northgatelinings@mailbox-example.com</p>
    </section>

    <section class="contact contact-business">
      <p>Mobile 0418 695 031</p>
      <p>ABN 51 847 213 906</p>
      <p>Commercial Plastering</p>
    </section>
  </main>
</body>
</html>
```